Need webdesign for service company that provides Car hiring service and transit service

We need a web design for a company that provides airport transit services and transport services including Limo, Corporate cars, Disability transit, Family transit service. We need is a simple and professional design.

Below is site which we like and also offer the same service http://www.ridelyntrek.com.au/

Reason: Waiting for the Feedback from multiple stakeholders. Need the time to select and approve the design

Target Market(s)

Tourism, Travel

Industry/Entity Type

Airport

Number of Pages Required

3 page

Font styles to use
Decorative
Script

Requirements
Must have
• Simple and Professional, Site we like http://www.ridelyntrek.com.au/ and also need to mobile friendly
Should not have
• Shouldn't have too many images

```html
<!DOCTYPE html>
<html lang="en">
<head>
<meta charset="utf-8">
<title>Ridewell – Private &amp; Business Transport</title>
<link href="https://fonts.googleapis.com/css2?family=Exo+2:wght@400;500&family=Open+Sans:wght@300;400;600&display=swap" rel="stylesheet">
<style>
:root{
  --ink:#222;
  --muted:#555;
  --soft:#777;
  --blue:#2b9fd4;
  --blue-dark:#1f8fc4;
  --dark:#1a1a1a;
  --band:#f1f1f1;
  --white:#fff;
  --line:#bdbdbd;
  --icon:#666;
}
*{box-sizing:border-box;margin:0;padding:0}
html,body{width:1164px;height:1200px;overflow:hidden;background:var(--white);font-family:"Open Sans",Arial,sans-serif;color:var(--ink)}
.page{position:relative;width:1164px;height:1200px}

/* header */
.site-header{position:absolute;top:0;left:0;width:1164px;height:128px}
.brand{position:absolute;display:flex;align-items:center;gap:10px}
.brand-mark{border:2px solid var(--ink);background:var(--white)}
.brand-name{font-family:"Exo 2",Arial,sans-serif;font-weight:400;color:var(--ink);letter-spacing:1px}
.site-header .brand{left:88px;top:36px}
.site-header .brand-mark{width:40px;height:40px}
.site-header .brand-name{font-size:30px}
.header-tools{position:absolute;right:86px;top:40px;display:flex;align-items:center;gap:12px}
.menu-toggle{width:30px;height:26px;display:flex;flex-direction:column;justify-content:space-between;margin-right:18px}
.menu-toggle span{display:block;height:5px;background:#333;border-radius:1px}
.round-btn{width:39px;height:39px;border:1px solid #555;border-radius:50%;display:flex;align-items:center;justify-content:center}

/* hero band */
.hero{position:absolute;top:128px;left:0;width:1164px;height:794px;background:radial-gradient(ellipse at center,#fbfbfb 0%,var(--band) 100%)}
.hero-title{position:absolute;top:78px;width:100%;text-align:center;font-family:"Exo 2",Arial,sans-serif;font-weight:400;font-size:33px;letter-spacing:1.5px;color:var(--ink)}
.hero-sub{position:absolute;top:119px;width:100%;text-align:center;font-family:"Exo 2",Arial,sans-serif;font-size:23px;color:#666;letter-spacing:.5px}
.hero-text{position:absolute;top:162px;left:118px;width:928px;text-align:center;font-size:14px;line-height:23px;color:var(--muted);font-weight:400}

/* quote panel */
.quote{position:absolute;top:304px;left:85px;width:387px;height:404px;background:linear-gradient(180deg,#1b1b1b 0%,#2a2a2a 45%,#141414 100%);color:var(--white)}
.quote h2{position:absolute;top:40px;left:37px;font-family:"Exo 2",Arial,sans-serif;font-weight:400;font-size:25px;letter-spacing:1px}
.field{position:absolute;left:38px;width:313px;height:36px;background:#efefef;display:flex;align-items:center}
.field-icon{width:36px;height:36px;background:var(--white);display:flex;align-items:center;justify-content:center}
.field-label{padding-left:12px;font-size:12.5px;color:#444}
.field.origin{top:93px}
.field.dest{top:140px}
.option{position:absolute;left:50px;display:flex;align-items:center;gap:10px;font-family:"Exo 2",Arial,sans-serif;font-size:15px}
.option.stops{top:203px}
.option.vehicles{top:235px}
.estimate{position:absolute;top:290px;left:37px;width:313px;height:55px;background:var(--blue);display:flex;align-items:center;justify-content:center;font-family:"Exo 2",Arial,sans-serif;font-size:20px;letter-spacing:.5px}
.note{position:absolute;top:352px;left:38px;font-size:11px}

/* tiles */
.tile{position:absolute;width:287px;height:197px;overflow:hidden}
.tile-caption{position:absolute;left:0;bottom:0;width:100%;height:40px;background:rgba(40,40,40,.55);color:var(--white);font-family:"Exo 2",Arial,sans-serif;font-size:15.5px;letter-spacing:.5px;padding:11px 20px 0}
.about{top:304px;left:481px;background:linear-gradient(135deg,#36a9dc,var(--blue-dark));color:var(--white);padding:26px 23px 0 23px}
.about h3{font-family:"Exo 2",Arial,sans-serif;font-weight:400;font-size:18px;letter-spacing:1px;margin-bottom:9px}
.about p{font-size:12px;line-height:18px;text-align:justify}
.member{top:304px;left:776px;background:linear-gradient(120deg,#c97a74 0%,#6b4f50 40%,#2a2a2e 70%,#8a8a8e 100%)}
.support{top:513px;left:481px;background:linear-gradient(110deg,#b9bcc0 0%,#d9d6d2 45%,#f2eeea 70%,#c8c4c0 100%)}
.transport{top:513px;left:776px;background:linear-gradient(160deg,#7d8d5b 0%,#e9e9ea 30%,#cfd0d2 70%,#9a9a9c 100%)}

/* footer */
.site-footer{position:absolute;top:922px;left:0;width:1164px;height:278px}
.site-footer .brand{left:88px;top:103px}
.site-footer .brand-mark{width:30px;height:30px}
.site-footer .brand-name{font-size:24px}
.footer-col{position:absolute;top:60px}
.footer-col h4{font-family:"Exo 2",Arial,sans-serif;font-weight:400;font-size:14px;letter-spacing:.5px;color:#333;margin-bottom:14px}
.contact{left:327px}
.contact p{font-size:11.5px;line-height:21px;color:var(--soft);padding-left:2px}
.mailing{left:611px}
.mailing p{font-size:11px;line-height:16px;color:var(--soft);width:200px;margin-bottom:9px}
.subscribe{display:flex;width:197px;height:31px}
.subscribe .email{flex:1;border:1px solid #ccc;border-right:none;font-size:12px;color:var(--soft);padding:8px 8px}
.subscribe .submit{width:55px;background:var(--blue);color:var(--white);font-size:12.5px;display:flex;align-items:center;justify-content:center}
.follow{left:887px}
.social{display:flex;gap:12px;margin-top:4px}
.social span{width:25px;height:25px;border-radius:4px;background:var(--icon)}
.footer-rule{position:absolute;top:212px;left:53px;width:992px;height:1px;background:var(--line)}
.copyright{position:absolute;top:236px;left:0;width:1090px;text-align:center;font-size:12.5px;color:#333}
</style>
</head>
<body>
<div class="page">

  <header class="site-header">
    <div class="brand">
      <span class="brand-mark"></span>
      <span class="brand-name">RIDEWELL</span>
    </div>
    <nav class="header-tools">
      <div class="menu-toggle" aria-label="Menu"><span></span><span></span><span></span></div>
      <div class="round-btn" aria-label="Call">
        <svg width="18" height="18" viewBox="0 0 24 24"><path d="M6.6 10.8a15.1 15.1 0 0 0 6.6 6.6l2.2-2.2a1 1 0 0 1 1-.25 11.4 11.4 0 0 0 3.6.57 1 1 0 0 1 1 1V20a1 1 0 0 1-1 1A17 17 0 0 1 3 4a1 1 0 0 1 1-1h3.5a1 1 0 0 1 1 1c0 1.25.2 2.45.57 3.6a1 1 0 0 1-.25 1z" fill="#2b9fd4"/></svg>
      </div>
      <div class="round-btn" aria-label="Search">
        <svg width="18" height="18" viewBox="0 0 24 24"><circle cx="10" cy="10" r="6.5" fill="none" stroke="#2b9fd4" stroke-width="2.6"/><line x1="15" y1="15" x2="21" y2="21" stroke="#2b9fd4" stroke-width="3" stroke-linecap="round"/></svg>
      </div>
    </nav>
  </header>

  <main class="hero">
    <h1 class="hero-title">PRIVATE &amp; BUSINESS</h1>
    <p class="hero-sub">Personalised Transport Service</p>
    <p class="hero-text">It is a long established fact that a reader will be distracted by the readable content of a page when looking at its layout. The point of using Lorem Ipsum is that it has a more-or-less normal distribution of letters, as opposed to using 'Content here, content here', making it look like readable English.Many desktop publishing packages and web page editors now use Lorem Ipsum as their default model text.</p>

    <section class="quote" role="img" aria-label="Dark photo of a luxury car on a city street behind the quote form">
      <h2>GET INSTANT QUOTE</h2>
      <div class="field origin">
        <span class="field-icon"><svg width="14" height="14" viewBox="0 0 14 14"><circle cx="7" cy="7" r="5.5" fill="none" stroke="#222" stroke-width="1.8"/></svg></span>
        <span class="field-label">Origin (public location or Exact Address)</span>
      </div>
      <div class="field dest">
        <span class="field-icon"><svg width="12" height="16" viewBox="0 0 12 16"><path d="M6 0a5.5 5.5 0 0 0-5.5 5.5C.5 9.6 6 16 6 16s5.5-6.4 5.5-10.5A5.5 5.5 0 0 0 6 0zm0 7.6a2 2 0 1 1 0-4 2 2 0 0 1 0 4z" fill="#222"/></svg></span>
        <span class="field-label">Destination (public location or Exact Address)</span>
      </div>
      <div class="option stops">
        <svg width="14" height="14" viewBox="0 0 14 14"><rect x="5" y="0" width="4" height="14" fill="#fff"/><rect x="0" y="5" width="14" height="4" fill="#fff"/></svg>
        <span>ADD STOPS</span>
      </div>
      <div class="option vehicles">
        <svg width="15" height="15" viewBox="0 0 16 16"><circle cx="8" cy="8" r="6.5" fill="none" stroke="#fff" stroke-width="2"/><circle cx="8" cy="8" r="3" fill="#fff"/></svg>
        <span>SHOW OTHER VEHICLES</span>
      </div>
      <div class="estimate">ESTIMATE FARE</div>
      <p class="note">*See price guide for extras</p>
    </section>

    <article class="tile about">
      <h3>ABOUT US</h3>
      <p>It is a long established fact that a reader will be distracted by the readable content of a page when looking at its layout. The point of using Lorem Ipsum is that it has a more-or-less normal distribution of letters, as opposed to using 'Content here,</p>
    </article>
    <article class="tile member" role="img" aria-label="Photo of a chauffeur in a suit standing beside a black sedan">
      <div class="tile-caption">BECOME A MEMBER</div>
    </article>
    <article class="tile support" role="img" aria-label="Photo of a support agent wearing a headset in an office">
      <div class="tile-caption">24/7 SUPPORT</div>
    </article>
    <article class="tile transport" role="img" aria-label="Photo of a passenger stepping out of a white limousine">
      <div class="tile-caption">TRANSPORT SERVICES</div>
    </article>
  </main>

  <footer class="site-footer">
    <div class="brand">
      <span class="brand-mark"></span>
      <span class="brand-name">RIDEWELL</span>
    </div>
    <div class="footer-col contact">
      <h4>CONTACT US</h4>
      <p>Address : 220 Harbour Lane</p>
      <p>Bayview QLD 4120</p>
      <p>Phone :&nbsp; 555-018-2400</p>
      <p>Email : hello@ridewell.example</p>
    </div>
    <div class="footer-col mailing">
      <h4>JOIN OUR MAILING LIST</h4>
      <p>Your about us information would fit here nicely.</p>
      <div class="subscribe">
        <span class="email">Email address</span>
        <span class="submit">Submit</span>
      </div>
    </div>
    <div class="footer-col follow">
      <h4>FOLLOW US OUT THERE</h4>
      <div class="social">
        <span aria-label="Social link 1"></span>
        <span aria-label="Social link 2"></span>
        <span aria-label="Social link 3"></span>
        <span aria-label="Social link 4"></span>
      </div>
    </div>
    <div class="footer-rule"></div>
    <p class="copyright">Copyright © 2017. All Rights Reserved</p>
  </footer>

</div>
</body>
</html>
```